Essential Oils and Chemical Free Skincare Packaging

We have a range of 100% organic 10ml essential oils and 10ml essential oil synergy blends and 50ml spritzer bottles plus chemical free skincare products including two serums, one cleanser, two moisturisers, a lip balm, an eye and lip cream and a body lotion that need new labels, boxes for the products with a fresh new look. Some of these products are in packs or gift packs as seen on the website. Our logo is attached, we love the logo colours. Our website is www.velis4.com. We have high quality, chemical-free and organic ingredients and amazingly effective products. The packaging now needs to reflect the contents and the prices of the precious ingredients. We think we would like to stick to the amber glass, thinking of black lids. Want it to feel professional, classy, high-end, classic and not fussy. Would love for the packaging to feel fresh, beautiful, natural, expensive... yet still affordable luxury. New packaging could be predominantly grey and white with flash of the green. Our customer is busy and health conscious. She does not need a lot of fuss but loves using beautiful products. Some of our tag lines include - 'Beauty is being yourself but with a sparkle.' and 'Self-care is your divine responsibility.' Velis4 brightens every morning from within.' Can you please look at the product jars and bottles as well as the boxes that the oils will be packaged in.

Target Market(s)

30-50yr females, business women, entrepreneurs, health conscious mum's all with an awareness around the importance of chemical-free and organic products and a love for health, fitness and real beauty.

Colors

Requirements
Must have
• Our logo and our logo colours incorporated. As mentioned could be predominantly silver/grey and white with splash of green. The bottles could even be printed in the one silver/grey colour directly onto the glass as an option. Or labels to wrap around the bottles. Boxes (which are separate to the bottles) containing the products to be inviting and speak luxury. Must be recyclable in alignment with our values.
Nice to have
• Not sure whether to look at printing on the glass direct or complete wrap around labels (which will no doubt be cheaper to create). Would love a number of design options and ideas that give that beautiful feel and would make our customer so excited to want these products. Our packaging is over 8 years old and we have grown significantly in this time. It would be nice to have a new fresh look that reflects the quality and amazing efficacy of these products.
• One suggestion regarding the packaging for the essential oils is to categorise them - so the floral oils like lavender, geranium, neroli and rose all have a certain colour or something on the packaging to distinguish them as floral oils. Then we have herbal, spicy, woody, grass and citrus categories too. This could be shown on the box as opposed to the bottle.
• We also have four kinds of synergy blends that are based on the four main personality types eg: Powerful, Playful, Peaceful and Precise. No one necessarily knows this unless I am speaking but the oil blends that fit in here are Powerful - Harbor & Thistle, Copper Drift and Willow & Ember. Playful - Lantern & Tide, Pebble & Frost and Moss & Flint. Peaceful - Velvet Dune, Orchard & Hollow and Cloud & Cinder. Precise - Marble & Thread, Canyon & Reed and Quill & Meadow.
• I also love to incorporate the four seasons and we have four one-off seasonal blends called Sail Away (winter), Drift On (spring), Hum Low (summer) and Stay Put (autumn).
• If there was a strong element of natural beauty with this new packaging that would be amazing.
Should not have
• Lots of different wild out there colours. We love nature, and plants and order and clarity. Should not have too much information or busyness. Needs to be simple, elegant, classy, classic, beautiful. Please do not go cottage/lavender farm industry looking.

```html
<!DOCTYPE html>
<html lang="en">
<head>
<meta charset="utf-8">
<title>Velis4 Herbal Essential Oil Label</title>
<link href="https://fonts.googleapis.com/css2?family=Marcellus&family=Noto+Serif:wght@400&family=Encode+Sans+Semi+Condensed:wght@500;600&display=swap" rel="stylesheet">
<style>
  :root {
    --label-green: #74ad3b;
    --label-green-light: #86bb4e;
    --label-green-dark: #66a030;
    --ink-white: #ffffff;
  }
  html, body {
    margin: 0;
    padding: 0;
    width: 906px;
    height: 1200px;
    overflow: hidden;
    background: var(--label-green);
  }
  .label {
    position: relative;
    width: 906px;
    height: 1200px;
    background: var(--label-green);
    color: var(--ink-white);
    overflow: hidden;
  }
  .label__pattern {
    position: absolute;
    inset: 0;
    background: radial-gradient(ellipse at 50% 45%, var(--label-green-light), var(--label-green) 60%, var(--label-green-dark));
  }
  .label__rule {
    position: absolute;
    left: 0;
    width: 906px;
    height: 7px;
    background: var(--ink-white);
  }
  .label__rule--top { top: 40px; }
  .label__rule--bottom { top: 1130px; height: 6px; }
  .brand {
    position: absolute;
    top: 250px;
    left: 0;
    width: 906px;
    text-align: center;
    font-family: "Marcellus", serif;
    font-size: 78px;
    letter-spacing: 5px;
    line-height: 1;
  }
  .tagline {
    position: absolute;
    top: 420px;
    left: 0;
    width: 906px;
    text-align: center;
    font-family: "Noto Serif", serif;
    font-size: 32px;
    line-height: 38px;
  }
  .category {
    position: absolute;
    top: 505px;
    left: 0;
    width: 906px;
    margin: 0;
    text-align: center;
    font-family: "Encode Sans Semi Condensed", sans-serif;
    font-weight: 500;
    font-size: 120px;
    line-height: 1;
  }
  .claim {
    position: absolute;
    top: 720px;
    left: 317px;
    width: 272px;
    height: 96px;
  }
  .claim__text {
    position: absolute;
    left: 4px;
    top: 16px;
    font-family: "Encode Sans Semi Condensed", sans-serif;
    font-weight: 600;
    line-height: 1;
  }
  .claim__percent { font-size: 28px; display: block; }
  .claim__sub { font-size: 11px; display: block; margin-top: 2px; }
  .claim__name { font-size: 21px; display: block; margin-top: 2px; }
  .claim__leaf {
    position: absolute;
    left: 168px;
    top: 0;
    width: 76px;
    height: 76px;
    border-radius: 10px;
    background: rgba(255, 255, 255, 0.35);
  }
  .claim__swoosh {
    position: absolute;
    left: 0;
    top: 80px;
  }
  .net-weight {
    position: absolute;
    top: 1113px;
    left: 338px;
    width: 230px;
    height: 40px;
    border-radius: 7px;
    background: var(--ink-white);
    display: flex;
    align-items: center;
    justify-content: center;
  }
  .net-weight span {
    width: 224px;
    height: 34px;
    border-radius: 5px;
    background: var(--label-green);
    font-family: "Encode Sans Semi Condensed", sans-serif;
    font-weight: 500;
    font-size: 26px;
    line-height: 34px;
    text-align: center;
    color: var(--ink-white);
  }
</style>
</head>
<body>
<main class="label">
  <div class="label__pattern" role="img" aria-label="Subtle tonal green leaf pattern across the label"></div>
  <div class="label__rule label__rule--top"></div>
  <div class="label__rule label__rule--bottom"></div>

  <div class="brand">VELIS4</div>
  <div class="tagline">Beauty Is Being Yourself<br>But With A Sparkle</div>
  <h1 class="category">Herbal</h1>

  <div class="claim">
    <div class="claim__text">
      <span class="claim__percent">100%</span>
      <span class="claim__sub">Pure Organic</span>
      <span class="claim__name">Essential Oil</span>
    </div>
    <div class="claim__leaf" role="img" aria-label="Leaf sprig emblem"></div>
    <svg class="claim__swoosh" width="272" height="14" viewBox="0 0 272 14">
      <path d="M2 8 Q120 14 268 3" stroke="#ffffff" stroke-width="3" fill="none"/>
    </svg>
  </div>

  <div class="net-weight"><span>Net Weight 10ml</span></div>
</main>
</body>
</html>
```